The Maplewood Family Clinic needs a Letterhead

We are a bilingual pediatric clinic located in Montreal, Canada.

Our english name is Maplewood Family Clinic
Our french name is Clinique du parc Verdelle

We offer complete care for children including general pediatric care, pediatric specialist care such as Ear, Nose and Throat, Urology, Neurology and Adolescent Medicine. We also have paramedical specialists such as psychologists, social workers, occupational therapists, speech and language pathologists.

The letterhead must use and be harmonious with our new logo. See Design #7150846. We need two types of letterhead. One for a the Logo and both english and french names on the top and the second with the list of current staff on the left. I have uploaded two old examples for you to see. Thanks and good luck.

Industry/Entity Type

Clinic

Font styles to use
Sans Serif

Colors
3176b5
9d9d9d

Requirements
Must have
• Include our logo.
Nice to have
• Most of our printing is done in black and white. So a grayscale design is fine.
I have included a color and grayscale versions of our logo.

We prefer clean modern designs.

```html
<!DOCTYPE html>
<html lang="en">
<head>
<meta charset="utf-8">
<title>Maplewood Family Clinic – Letterhead</title>
<link rel="stylesheet" href="https://fonts.googleapis.com/css2?family=Arimo:wght@400&family=Open+Sans:wght@300;400&display=swap">
<style>
  :root {
    --backdrop: #ebebeb;
    --paper: #ffffff;
    --sidebar: #d3d3d3;
    --sidebar-foot: #7b7b7b;
    --sidebar-text: #ffffff;
    --heading-ink: #5a5a5a;
    --body-ink: #1e1e1e;
  }
  * { box-sizing: border-box; margin: 0; padding: 0; }
  html, body { width: 1200px; height: 1000px; overflow: hidden; }
  body {
    background: var(--backdrop);
    font-family: "Arimo", Arial, sans-serif;
    position: relative;
  }
  .letterhead {
    position: absolute;
    left: 237px; top: 30px;
    width: 726px; height: 940px;
    background: var(--paper);
    box-shadow: 0 2px 10px rgba(0,0,0,.15);
    display: flex;
  }
  .staff-sidebar {
    width: 150px;
    background: var(--sidebar);
    position: relative;
    text-align: center;
    color: var(--sidebar-text);
    font-family: "Open Sans", Arial, sans-serif;
    font-size: 8.5px;
    line-height: 1.45;
  }
  .clinic-mark {
    display: flex; flex-direction: column; align-items: center; gap: 6px;
    padding: 26px 10px 0;
    font-size: 12px; font-weight: 400; line-height: 1.2;
  }
  .clinic-mark .dot {
    width: 34px; height: 34px; border-radius: 50%;
    border: 3px solid var(--sidebar-text);
  }
  .staff-list { margin-top: 44px; }
  .staff-group { margin-bottom: 22px; }
  .staff-group h3 { font-size: 8.5px; font-weight: 400; margin-bottom: 2px; }
  .staff-group p { opacity: .95; }
  .sidebar-foot {
    position: absolute; left: 0; bottom: 0;
    width: 100%; height: 62px;
    background: var(--sidebar-foot);
  }
  .letter {
    flex: 1;
    padding: 36px 52px 0 50px;
    color: var(--body-ink);
    font-size: 11.2px;
    line-height: 1.32;
  }
  .clinic-name {
    font-family: "Open Sans", Arial, sans-serif;
    font-weight: 300;
    font-size: 20.5px;
    color: var(--heading-ink);
    letter-spacing: .2px;
    margin-bottom: 42px;
  }
  .sender, .recipient { margin-bottom: 14px; }
  .salutation { margin: 30px 0 10px; }
  .letter-body p { margin-bottom: 14px; text-align: justify; text-indent: 100px; }
  .closing { margin-top: 30px; }
</style>
</head>
<body>
  <main class="letterhead">
    <aside class="staff-sidebar">
      <div class="clinic-mark">
        <span class="dot"></span>
        <span>Maplewood<br>Family Clinic</span>
      </div>
      <div class="staff-list">
        <section class="staff-group">
          <h3>Adresse • Address</h3>
          <p>4200 Rue Verdelle<br>Suite 210<br>Montréal, QC<br>H2X 1Y4</p>
          <p style="margin-top:10px">Tél. 514 555 0142<br>Fax 514 555 0143</p>
        </section>
        <section class="staff-group">
          <h3>Pédiatrie • Pediatrics</h3>
          <p>Dr. L. Gagnon<br>Dr. M. Roy<br>Dr. S. Côté<br>Dr. J. Bouchard<br>Dr. E. Morin<br>Dr. C. Pelletier</p>
        </section>
        <section class="staff-group">
          <h3>Neurologie • Neurologist</h3>
          <p>Dr. P. Lavoie</p>
        </section>
        <section class="staff-group">
          <h3>O.R.L. • E.N.T.</h3>
          <p>Dr. R. Fortin</p>
        </section>
        <section class="staff-group">
          <h3>Urologie • Urologist</h3>
          <p>Dr. N. Girard</p>
        </section>
        <section class="staff-group">
          <h3>Psychologue • Psychologists</h3>
          <p>Dr. A. Caron<br>Dr. D. Ouellet</p>
        </section>
        <section class="staff-group">
          <h3>Thérapeute • Therapist</h3>
          <p>K. Bélanger</p>
        </section>
        <section class="staff-group">
          <h3>Diététiste • Dietician</h3>
          <p>V. Lefebvre</p>
        </section>
        <section class="staff-group">
          <h3>Gérante • Manager</h3>
          <p>T. Cloutier</p>
        </section>
      </div>
      <div class="sidebar-foot"></div>
    </aside>

    <article class="letter">
      <h1 class="clinic-name">Maplewood Family Clinic • Clinique du parc Verdelle</h1>
      <address class="sender" style="font-style:normal">
        Dr. Daniel Hart<br>48 Elm Row<br>Riverton, NY 10001<br>April 17, 2016
      </address>
      <address class="recipient" style="font-style:normal">
        Dr. Helen Marsh<br>Westbrook University Medical Center<br>90 Harbor Ave.<br>Westbrook, CA 90210
      </address>
      <p class="salutation">Dear Dr. Marsh,</p>
      <div class="letter-body">
        <p>Lorem ipsum dolor sit amet, consectetuer adipiscing elit. Aenean commodo ligula eget dolor. Aenean massa. Cum sociis natoque penatibus et magnis dis parturient montes, nascetur ridiculus mus. Donec quam felis, ultricies nec, pellentesque eu, pretium quis, sem. Nulla consequat massa quis enim. Donec pede justo, fringilla vel, aliquet nec, vulputate eget, arcu. In enim justo, rhoncus ut, imperdiet a, venenatis vitae, justo. Nullam dictum felis eu pede mollis pretium.</p>
        <p>Integer tincidunt. Cras dapibus. Vivamus elementum semper nisi. Aenean vulputate eleifend tellus. Aenean leo ligula, porttitor eu, consequat vitae, eleifend ac, enim. Aliquam lorem ante, dapibus in, viverra quis, feugiat a, tellus. Phasellus viverra nulla ut metus varius laoreet. Quisque rutrum. Aenean imperdiet. Etiam ultricies nisi vel augue. Curabitur ullamcorper ultricies nisi. Nam eget dui. Etiam rhoncus.</p>
        <p>Maecenas tempus, tellus eget condimentum rhoncus, sem quam semper libero, sit amet adipiscing sem neque sed ipsum. Nam quam nunc, blandit vel, luctus pulvinar, hendrerit id, lorem. Maecenas nec odio et ante tincidunt tempus. Donec vitae sapien ut libero venenatis faucibus. Nullam quis ante. Etiam sit amet orci eget eros faucibus tincidunt. Duis leo. Sed fringilla mauris sit amet nibh. Donec sodales sagittis magna. Sed consequat, leo eget bibendum sodales, augue velit cursus nunc.</p>
        <p>Lorem ipsum dolor sit amet, consectetuer adipiscing elit. Aenean commodo ligula eget dolor. Aenean massa. Cum sociis natoque penatibus et magnis dis parturient montes, nascetur ridiculus mus. Donec quam felis, ultricies nec, pellentesque eu, pretium quis, sem. Nulla consequat massa quis enim. Donec pede justo, fringilla vel, aliquet nec, vulputate eget, arcu.</p>
      </div>
      <p class="closing">Kind regards,<br>Dr. Daniel Hart</p>
    </article>
  </main>
</body>
</html>
```